EB-5 Regional Center needs a Web design

Tallowmere Funding Partners is an expanding EB-r regional center. We have been successful in sponsoring multiple projects of third-party developers and placing EB-5, B-1, and Private Investments into multiple projects.

We are now partnering directly with project developers in the energy and healthcare to raise foreign capital for projects in those industries. The foreign capital is used as project equity and our collective balance sheets are used to guarantee debt to complete the funding of the projects.

We need a web site where we can post our company credentials, the bios of each partner, a document page for each of our projects where we can post specific project related documents which foreign investors can read, and we will need a section where foreign investors can fill out investor forms confirming that they are qualified investors and leaving their contact so that our agents and executives can make contact.

The final design should reflect the exceptional experience of the partners and our financial strength and stability.

We do have a logo we would want to use on the web design.

Target Market(s)

EB-5 Investors, B-1 Investors, Private Equity and other investors seeking quality investment in job creating US projects.

Coding

Number of Pages Required

5+ page

Font styles to use
Sans Serif

Requirements
Must have
• Pages to display company info, partner bios, projects completed, and a projects in-process page where we can post documents and info on projects for which we are seeking foreign investment. We also need a section where investors can enter their qualifying personal information and leave contact information for us.

```html
<!DOCTYPE html>
<html lang="en">
<head>
<meta charset="utf-8">
<title>Tallowmere Funding Partners</title>
<link href="https://fonts.googleapis.com/css2?family=IBM+Plex+Sans:wght@400;500;600;700&family=Lato:wght@400;700;900&display=swap" rel="stylesheet">
<style>
:root{
  --gold:#e0a526;
  --gold-dark:#c98f14;
  --ink:#2b2b2b;
  --ink-deep:#1f1f1f;
  --nav:#5b5b5b;
  --text:#3d3d3d;
  --muted:#6a6a6a;
  --line:#d9d9d9;
  --paper:#ffffff;
  --soft:#efefef;
}
*{box-sizing:border-box;margin:0;padding:0}
html,body{width:1200px;height:5367px;overflow:hidden}
body{position:relative;background:var(--paper);font-family:'Lato',sans-serif;color:var(--text)}
.abs{position:absolute}
.heading{font-family:'IBM Plex Sans',sans-serif;font-weight:700;color:#fff;letter-spacing:1px;text-align:center}
.divider{position:absolute;left:50%;transform:translateX(-50%);width:170px;height:12px}
.btn{position:absolute;background:var(--gold);color:#fff;font-family:'Lato',sans-serif;font-weight:900;font-size:15px;text-transform:uppercase;display:flex;align-items:center;justify-content:center;border-radius:3px}

/* top nav */
.topnav{left:0;top:0;width:1200px;height:46px;background:var(--nav);display:flex;justify-content:center}
.topnav a{color:#fff;font-size:13.5px;font-weight:700;text-decoration:none;padding:0 22px;line-height:46px}
.topnav a.active{background:#fff;color:var(--nav)}
.header{left:0;top:46px;width:1200px;height:100px;background:#fff}
.brand{left:146px;top:34px;display:flex;align-items:center;gap:12px;white-space:nowrap}
.brand-mark{width:30px;height:30px;background:#7a7a7a}
.brand-name{font-family:'IBM Plex Sans',sans-serif;font-weight:600;font-size:26px;color:#6d6d6d}
.ask{left:624px;top:30px;text-align:right;width:210px;white-space:nowrap}
.ask small{display:block;font-size:15px;line-height:20px;color:#444}
.ask strong{display:block;font-size:24px;line-height:28px;color:#222;font-weight:700}
.phone-dot{left:845px;top:36px;width:38px;height:38px;border-radius:50%;background:var(--gold)}
.client{left:909px;top:34px;width:146px;height:42px;border:2px solid #333;font-weight:900;font-size:14px;display:flex;align-items:center;justify-content:center;color:#222;white-space:nowrap}

/* hero */
.hero{left:0;top:146px;width:1200px;height:664px;clip-path:polygon(0 0,100% 0,100% 91%,50% 100%,0 91%)}
.hero-photo{width:100%;height:100%;background:linear-gradient(120deg,#6a4a32 0%,#a88a6e 35%,#c9b49a 55%,#7b6a58 80%,#4a3b2e 100%)}
.hero-shade{left:0;top:0;width:100%;height:100%;background:rgba(0,0,0,.25)}
.hero h1{position:absolute;left:0;top:248px;width:1200px;font-family:'IBM Plex Sans',sans-serif;font-weight:700;font-size:58px;line-height:66px;color:#fff;text-align:center;text-shadow:0 2px 6px rgba(0,0,0,.5)}
.arrow{width:30px;height:30px;border-radius:50%;background:rgba(255,255,255,.85);display:flex;align-items:center;justify-content:center}

/* welcome */
.welcome-rule{left:600px;top:820px;width:1px;height:420px;background:#eee}
.welcome small{display:block;font-size:22px;color:#555;letter-spacing:.5px}
.welcome h2{font-family:'IBM Plex Sans',sans-serif;font-weight:700;font-size:29px;line-height:34px;color:#222;letter-spacing:.5px}
.bar{width:72px;height:4px;background:#555;margin:16px 0 22px}
.body-copy{font-size:14.5px;line-height:24px;color:#444}

/* services */
.services{left:0;top:1250px;width:1200px;height:870px;background:var(--ink);clip-path:polygon(0 9.5%,50% 0,100% 9.5%,100% 90.5%,50% 100%,0 90.5%)}
.services-lead h3{font-family:'IBM Plex Sans',sans-serif;font-weight:700;font-size:28px;line-height:38px;color:#fff;letter-spacing:1px}
.services-lead .gold-bar{width:72px;height:4px;background:var(--gold);margin:20px 0 24px}
.services-lead p{font-size:13.5px;line-height:23px;color:#d5d5d5}
.card{position:absolute;width:288px;height:217px;background:#fff;padding:22px 24px}
.card .ic{position:absolute;left:26px;top:22px;width:64px;height:64px;border-radius:50%;background:var(--gold);border:4px solid #f3d58f}
.card h4{position:absolute;left:112px;top:30px;font-family:'IBM Plex Sans',sans-serif;font-size:16.5px;line-height:21px;font-weight:600;color:#222}
.card p{position:absolute;left:26px;top:98px;width:240px;font-size:13px;line-height:21px;color:#444}

/* bios */
.bios-stripe{left:138px;top:2200px;width:24px;height:494px;background:repeating-linear-gradient(45deg,#bbb 0 2px,#fff 2px 6px)}
.bios-stripe2{left:138px;top:2200px;width:420px;height:14px;background:repeating-linear-gradient(45deg,#bbb 0 2px,#fff 2px 6px)}
.bios-photo{left:148px;top:2208px;width:410px;height:486px;background:linear-gradient(160deg,#e9e4dd 0%,#cfc4b6 40%,#8aa0bd 70%,#6f7f96 100%)}
.bios h2{font-family:'IBM Plex Sans',sans-serif;font-size:38px;font-weight:600;color:#222}
.infobar{left:392px;top:2600px;width:670px;height:94px;background:#ececec;display:flex}
.infobar div{flex:1;display:flex;align-items:center;gap:10px;padding-left:24px;font-size:13.5px;line-height:20px;color:#555;border-right:1px solid #fff;white-space:nowrap}
.infobar div:last-child{border-right:none;flex:1.3}

/* testimonial */
.testi{left:0;top:2800px;width:1200px;height:620px;clip-path:polygon(0 7%,50% 0,100% 7%,100% 93%,50% 100%,0 93%)}
.testi-photo{width:100%;height:100%;background:linear-gradient(110deg,#3a3a3a 0%,#6b6b6b 40%,#555 65%,#2e2e2e 100%)}
.quote-card{left:246px;top:3025px;width:708px;height:194px;background:#fff;border-radius:10px}
.quote-card p{position:absolute;left:78px;top:36px;width:590px;font-size:13.5px;line-height:17px;color:#333}
.quote-card .who{position:absolute;left:0;top:142px;width:100%;text-align:center;font-family:'IBM Plex Sans',sans-serif;font-weight:700;font-size:18px;letter-spacing:1px;color:#222}
.who span{color:var(--gold)}
.avatar{position:absolute;top:3258px;width:48px;height:48px;border-radius:50%;border:3px solid #fff;background:#8a8a8a}

/* projects */
.tile{position:absolute}
.tile.gold{background:var(--gold);color:#fff;text-align:center}

/* quote */
.quote-sec{left:0;top:4340px;width:1200px;height:712px;background:var(--ink-deep);clip-path:polygon(0 8.5%,100% 0,100% 100%,0 100%)}
.field{position:absolute;left:221px;width:364px;height:36px;border:1px solid #9a9a9a;color:#fff;font-size:12px;padding:10px 14px}
.msg{left:604px;top:4631px;width:373px;height:192px;border:1px solid #9a9a9a;color:#fff;font-size:12px;padding:10px 14px}
.skyline{left:0;top:4990px;width:1200px;height:62px;background:linear-gradient(#fff 0,#fff 12%,#2a2a2a 12%,#2a2a2a 100%)}

/* footer */
.foot-contact{top:5118px;display:flex;align-items:center;gap:12px;font-size:15px;line-height:21px;color:#555;white-space:nowrap}
.foot-links{left:0;top:5193px;width:1200px;text-align:center;font-size:15px;color:#333}
.copy{left:0;top:5230px;width:1200px;text-align:center;font-size:15px;color:#333}
.social{position:absolute;top:5282px;width:32px;height:32px;border-radius:50%;border:2px solid #333}
</style>
</head>
<body>

<nav class="abs topnav">
  <a class="active">HOME</a><a>ABOUT</a><a>OUR PROJECTS</a><a>OUR SERVICES</a><a>RESOURCES</a><a>EVENTS</a><a>CONTACT US</a>
</nav>

<header class="abs header">
  <div class="abs brand"><span class="brand-mark"></span><span class="brand-name">Tallowmere Funding Partners</span></div>
  <div class="abs ask"><small>Have any Question?</small><strong>800-555-0142</strong></div>
  <div class="abs phone-dot"><svg width="38" height="38" viewBox="0 0 38 38"><path d="M13 11c2 0 3 4 2 5l-2 1c1 3 3 5 6 6l1-2c1-1 5 0 5 2 0 2-2 4-4 4-7-1-12-6-12-12 0-2 2-4 4-4z" fill="#fff"/></svg></div>
  <div class="abs client">CLIENT LOGIN</div>
</header>

<section class="abs hero">
  <div class="hero-photo" role="img" aria-label="Advisors reviewing documents with clients around a laptop"></div>
  <div class="abs hero-shade"></div>
  <div class="abs arrow" style="left:70px;top:248px"><svg width="12" height="12"><path d="M8 1L3 6l5 5" stroke="#333" stroke-width="2" fill="none"/></svg></div>
  <div class="abs arrow" style="left:1100px;top:248px"><svg width="12" height="12"><path d="M4 1l5 5-5 5" stroke="#333" stroke-width="2" fill="none"/></svg></div>
  <h1>TALLOWMERE<br>FUNDING PARTNERS</h1>
  <div class="btn" style="left:505px;top:404px;width:190px;height:44px">FIND OUT MORE</div>
</section>

<section class="welcome">
  <div class="abs welcome-rule"></div>
  <div class="abs" style="left:142px;top:864px;width:370px">
    <small>WELCOME TO</small>
    <h2>TALLOWMERE FUNDING PARTNERS</h2>
    <div class="bar"></div>
    <p class="body-copy">Sed ut perspiciatis unde omnis iste natus error sit voluptatem accusantium doloremque laudantium, totam rem aperiam, eaque ipsa quae ab illo inventore veritatis et quasi architecto beatae vitae dicta sunt explicabo. Nemo enim ipsam voluptatem quia voluptas sit aspernatur aut odit aut fugit, sed quia consequuntur magni dolores eos qui ratione voluptatem sequi nesciunt. Neque porro quisquam est, qui dolorem ipsum quia dolor sit amet,</p>
  </div>
  <svg class="abs" style="left:670px;top:858px" width="390" height="380" viewBox="0 0 390 380" role="img" aria-label="Close-up of hands with a calculator and financial papers">
    <defs><linearGradient id="wg" x1="0" y1="0" x2="1" y2="1"><stop offset="0" stop-color="#e8e2da"/><stop offset=".5" stop-color="#c9b8a6"/><stop offset="1" stop-color="#9aa8b8"/></linearGradient></defs>
    <polygon points="195,0 390,190 195,380 0,190" fill="url(#wg)"/>
  </svg>
</section>

<section class="abs services">
  <div class="heading abs" style="left:0;top:100px;width:1200px;font-size:35px">OUR SERVICES</div>
  <svg class="divider" style="top:172px" viewBox="0 0 170 12"><line x1="0" y1="6" x2="70" y2="6" stroke="#ddd"/><line x1="100" y1="6" x2="170" y2="6" stroke="#ddd"/><rect x="80" y="1" width="10" height="10" transform="rotate(45 85 6)" fill="#ddd"/></svg>
  <div class="abs services-lead" style="left:144px;top:296px;width:280px">
    <h3>NEMO ENIM IPSAM VOLUPTATEM QUIA VOLUPTAS</h3>
    <div class="gold-bar"></div>
    <p>Sed ut perspiciatis unde omnis iste natus error sit voluptatem accusantium doloremque laudantium, totam rem aperiam, eaque ipsa quae ab illo inventore veritatis et quasi architecto beatae vitae dicta sunt explicabo.</p>
    <div class="btn" style="position:relative;margin-top:24px;width:130px;height:40px;font-size:13px">LEARN MORE</div>
  </div>
  <div class="card" style="left:458px;top:246px"><span class="ic"></span><h4>Nemo enim psam voluptatem</h4><p>Lorem ipsum dolor sit amet, cotetur adipiscing elit, sed do eiusmod tempor incididunt ut labore et dolore magna aliqua. Ut enim ad minim</p></div>
  <div class="card" style="left:767px;top:246px"><span class="ic"></span><h4>Nemo enim psam voluptatem</h4><p>Lorem ipsum dolor sit amet, cotetur adipiscing elit, sed do eiusmod tempor incididunt ut labore et dolore magna aliqua. Ut enim ad minim</p></div>
  <div class="card" style="left:458px;top:485px"><span class="ic"></span><h4>Nemo enim psam voluptatem</h4><p>Lorem ipsum dolor sit amet, cotetur adipiscing elit, sed do eiusmod tempor incididunt ut labore et dolore magna aliqua. Ut enim ad minim</p></div>
  <div class="card" style="left:767px;top:485px"><span class="ic"></span><h4>Nemo enim psam voluptatem</h4><p>Lorem ipsum dolor sit amet, cotetur adipiscing elit, sed do eiusmod tempor incididunt ut labore et dolore magna aliqua. Ut enim ad minim</p></div>
</section>

<section class="bios">
  <div class="abs bios-stripe"></div><div class="abs bios-stripe2"></div>
  <div class="abs bios-photo" role="img" aria-label="Smiling partner with glasses working at a laptop"></div>
  <div class="abs" style="left:604px;top:2236px;width:440px">
    <h2>Partner Bios</h2>
    <div style="width:110px;height:3px;background:#333;margin:14px 0 26px"></div>
    <p class="body-copy" style="font-size:14px">Sed ut perspiciatis unde omnis iste natus error sit voluptatem accsantium doloremque laudantium, totam rem aperiam, eaque ipsa quae ab illo inventore veritatis et quasi architecto beatae vitae dicta sunt explicabo. Nemo enim ipsam voluptatem quia voluptas sit aatur aut odit aut fugit, sed quia consequuntur magni dolores eos qui ratine voluptatem sequi nesciunt. Neque porro quisquam est, qui dolorem ipsum quia dolor</p>
  </div>
  <div class="btn" style="left:604px;top:2518px;width:146px;height:40px;font-size:14px">READ MORE</div>
  <div class="abs infobar">
    <div><svg width="16" height="20"><path d="M8 1a6 6 0 0 1 6 6c0 5-6 12-6 12S2 12 2 7a6 6 0 0 1 6-6z" fill="none" stroke="#e0a526" stroke-width="1.6"/><circle cx="8" cy="7" r="2" fill="#e0a526"/></svg><span>18 Larkspur Way,<br>Fernvale, 4021</span></div>
    <div><svg width="18" height="18"><path d="M4 2c2 0 3 3 2 4l-1 1c1 2 2 4 5 5l1-1c1-1 4 0 4 2 0 1-2 3-3 3C6 16 2 11 2 5c0-2 1-3 2-3z" fill="none" stroke="#e0a526" stroke-width="1.4"/></svg><span>Phone:<br>(808) 5550 1877</span></div>
    <div><svg width="18" height="14"><rect x="1" y="1" width="16" height="12" fill="none" stroke="#e0a526" stroke-width="1.4"/><path d="M1 1l8 7 8-7" fill="none" stroke="#e0a526" stroke-width="1.4"/></svg><span>E-mail:<br>info@tallowmerefunding.com</span></div>
  </div>
</section>

<section class="abs testi">
  <div class="testi-photo" role="img" aria-label="Grayscale meeting of colleagues around a table"></div>
  <div class="heading abs" style="left:0;top:100px;width:1200px;font-size:35px">TESTIMONIAL</div>
  <svg class="divider" style="top:162px" viewBox="0 0 170 12"><line x1="0" y1="6" x2="70" y2="6" stroke="#ddd"/><line x1="100" y1="6" x2="170" y2="6" stroke="#ddd"/><rect x="80" y="1" width="10" height="10" transform="rotate(45 85 6)" fill="#ddd"/></svg>
</section>
<div class="abs quote-card">
  <svg class="abs" style="left:30px;top:30px" width="36" height="28" viewBox="0 0 36 28"><path d="M2 26V16C2 8 7 3 14 1l1 3c-4 2-6 5-6 9h6v13zM20 26V16c0-8 5-13 12-15l1 3c-4 2-6 5-6 9h6v13z" fill="#555"/></svg>
  <p>Lorem ipsum dolor sit amet, consectetur adipisicing elit, sed do eiusmod tempor incididunt ut labore et dolore magna aliqua. Ut enim ad minim veniam. Quis nostrud exercitation ullamco laboris nisi ut aliquip ex ea commodo consequat. Duis aute irure dolor.Lorem ipsum dolor sit amet, consectetur adipisicing elit, sed do eiusmod tempor incididunt ut labore et dolore magna aliqua. Ut enim ad minim veniam.</p>
  <div class="who"><span>Mara Linden</span> | Tallowmere</div>
  <svg class="abs" style="left:272px;top:192px" width="24" height="14"><path d="M0 0h24L12 14z" fill="#fff"/></svg>
</div>
<div class="avatar" style="left:521px" role="img" aria-label="Client portrait"></div>
<div class="avatar" style="left:593px" role="img" aria-label="Client portrait"></div>
<div class="avatar" style="left:665px" role="img" aria-label="Client portrait"></div>

<section class="projects">
  <div class="heading abs" style="left:0;top:3476px;width:1200px;font-size:35px;color:#222">OUR PROJECT</div>
  <svg class="divider" style="top:3548px" viewBox="0 0 170 12"><line x1="0" y1="6" x2="70" y2="6" stroke="#444"/><line x1="100" y1="6" x2="170" y2="6" stroke="#444"/><rect x="80" y="1" width="10" height="10" transform="rotate(45 85 6)" fill="#444"/></svg>
  <div class="tile" style="left:144px;top:3604px;width:300px;height:306px;background:linear-gradient(135deg,#d8d8d8,#8c8c8c)" role="img" aria-label="Man working on a laptop in an office"></div>
  <div class="tile" style="left:460px;top:3604px;width:300px;height:306px;background:linear-gradient(135deg,#bfbfbf,#4a4a4a)" role="img" aria-label="Hand with a pen over data overlays"></div>
  <div class="tile gold" style="left:773px;top:3604px;width:281px;height:306px">
    <div style="width:44px;height:44px;background:#fff;opacity:.85;margin:44px auto 0"></div>
    <div style="font-family:'IBM Plex Sans',sans-serif;font-weight:600;font-size:13px;line-height:19px;margin-top:46px">NEMO ENIM IPSAM<br>VOLUPTATEM QUIA VOLUPTAS</div>
    <div style="font-size:13px;line-height:22px;margin:12px 36px 0;color:#fff3d6">Sed ut perspiciatis unde omnis iste natus voluptatem accusantium doloremque laudantium</div>
    <div style="margin:14px auto 0;width:112px;height:32px;border:2px solid #fff;font-size:11px;font-weight:900;line-height:28px">READ MORE</div>
  </div>
  <div class="tile" style="left:144px;top:3925px;width:300px;height:306px;background:linear-gradient(135deg,#9a9a9a,#3a3a3a)" role="img" aria-label="Calculator and charts on a desk"></div>
  <div class="tile" style="left:460px;top:3925px;width:300px;height:306px;background:linear-gradient(135deg,#cfcfcf,#707070)" role="img" aria-label="Smiling man reviewing documents"></div>
  <div class="tile" style="left:773px;top:3925px;width:281px;height:306px;background:linear-gradient(135deg,#e6e6e6,#8a8a8a)" role="img" aria-label="Overhead view of laptop and paperwork"></div>
</section>

<div class="abs quote-sec"></div>
<section class="quote">
  <div class="heading abs" style="left:0;top:4508px;width:1200px;font-size:35px">REQUEST A QUOTE</div>
  <svg class="divider" style="top:4572px" viewBox="0 0 170 12"><line x1="0" y1="6" x2="70" y2="6" stroke="#ddd"/><line x1="100" y1="6" x2="170" y2="6" stroke="#ddd"/><rect x="80" y="1" width="10" height="10" transform="rotate(45 85 6)" fill="#ddd"/></svg>
  <div class="field" style="top:4631px">Name</div>
  <div class="field" style="top:4683px">Email</div>
  <div class="field" style="top:4735px">Phone</div>
  <div class="field" style="top:4785px">Subject</div>
  <div class="abs msg">Message</div>
  <div class="btn" style="left:525px;top:4856px;width:156px;height:44px;font-size:17px">SUBMIT</div>
</section>
<div class="abs skyline" role="img" aria-label="City skyline silhouette"></div>

<footer>
  <div class="abs foot-contact" style="left:240px"><svg width="18" height="22"><path d="M9 1a7 7 0 0 1 7 7c0 6-7 13-7 13S2 14 2 8a7 7 0 0 1 7-7z" fill="none" stroke="#e0a526" stroke-width="1.6"/><circle cx="9" cy="8" r="2.4" fill="#e0a526"/></svg><span style="margin-left:10px">18 Larkspur Way,<br>Fernvale, 4021</span></div>
  <div class="abs foot-contact" style="left:478px"><svg width="20" height="20"><path d="M4 2c2 0 3 3 2 4l-1 1c1 2 3 5 6 6l1-1c1-1 4 0 4 2 0 1-2 3-3 3C6 17 2 12 2 6c0-2 1-4 2-4z" fill="none" stroke="#e0a526" stroke-width="1.4"/></svg><span style="margin-left:12px">Phone:<br>(808) 5550 1877</span></div>
  <div class="abs foot-contact" style="left:714px"><svg width="20" height="15"><rect x="1" y="1" width="18" height="13" fill="none" stroke="#e0a526" stroke-width="1.4"/><path d="M1 1l9 7 9-7" fill="none" stroke="#e0a526" stroke-width="1.4"/></svg><span style="margin-left:8px">E-mail:<br>info@tallowmerefunding.com</span></div>
  <div class="abs" style="left:685px;top:5120px;width:1px;height:48px;background:#ccc"></div>
  <div class="abs" style="left:448px;top:5120px;width:1px;height:48px;background:#ccc"></div>
  <div class="abs foot-links">Home &nbsp;|&nbsp; About &nbsp;|&nbsp; Project &nbsp;|&nbsp; Services &nbsp;|&nbsp; Partner Bios &nbsp;|&nbsp; Contact</div>
  <div class="abs copy">© 2020 Tallowmere Funding Partners. All Rights Reserved.</div>
  <span class="social" style="left:528px"></span>
  <span class="social" style="left:566px"></span>
  <span class="social" style="left:604px"></span>
  <span class="social" style="left:642px"></span>
</footer>

</body>
</html>
```